Orvek Electric Construction Power Runs Deep!

We have an up coming meeting with a developer and general contractor. This card must bring out the best in my business. My business is an up and coming MDBE certified electrical contactor. I need a very powerful card to represent me business that we be bold and represent what I am about. POWER RUNS DEEP!

Target Market(s)

General Contractors, developers and property owners

Industry/Entity Type

Electrical

Contact Information for Business Card

great card that really brings out my bussiness

Colors
0355a3
3276b5
0393ce
34a6d7

Requirements
Must have
• Great design
Nice to have
• very different and noticeable card
Should not have
• open to anything

```html
<!DOCTYPE html>
<html lang="en">
<head>
<meta charset="utf-8">
<title>Orvek Electric Construction – Business Card</title>
<link rel="stylesheet" href="https://fonts.googleapis.com/css2?family=Arimo:wght@400&family=Quicksand:wght@600;700&display=swap">
<style>
  :root {
    --navy: #0355a3;
    --mid-blue: #3276b5;
    --sky: #0393ce;
    --light-sky: #34a6d7;
    --white: #ffffff;
    --backdrop: #e9ecef;
  }
  * { box-sizing: border-box; margin: 0; padding: 0; }
  html, body { width: 1200px; height: 800px; overflow: hidden; }
  body {
    background: var(--backdrop);
    display: flex;
    align-items: center;
    justify-content: center;
    gap: 40px;
  }
  .card {
    position: relative;
    width: 540px;
    height: 309px;
    background: var(--white);
    overflow: hidden;
    box-shadow: 0 6px 18px rgba(0,0,0,0.15);
  }
  .card-art { position: absolute; inset: 0; width: 100%; height: 100%; }

  .brand {
    position: absolute;
    display: flex;
    align-items: center;
    gap: 10px;
    font-family: "Arimo", Arial, sans-serif;
    font-weight: 400;
    color: var(--sky);
    white-space: nowrap;
    line-height: 1;
  }
  .brand-mark { background: var(--navy); flex: none; }

  .card-front .brand { left: 50%; top: 162px; transform: translateX(-50%); font-size: 24px; }
  .card-front .brand-mark { width: 28px; height: 28px; }

  .card-back .brand { left: 160px; top: 50px; font-size: 15px; }
  .card-back .brand-mark { width: 18px; height: 18px; }

  .holder {
    position: absolute;
    left: 40px;
    top: 190px;
    color: var(--white);
    font-family: "Quicksand", sans-serif;
  }
  .holder-name { font-size: 22px; font-weight: 700; line-height: 1; }
  .holder-role { font-size: 12px; font-weight: 600; margin-top: 2px; }

  .contact-list {
    position: absolute;
    left: 322px;
    top: 108px;
    list-style: none;
    color: var(--white);
    font-family: "Quicksand", sans-serif;
    font-weight: 600;
    font-size: 11px;
    line-height: 1.35;
  }
  .contact-list li { display: flex; gap: 7px; align-items: flex-start; margin-bottom: 4px; }
  .contact-icon { width: 12px; height: 12px; flex: none; margin-top: 1px; fill: var(--white); }
</style>
</head>
<body>

  <section class="card card-front" aria-label="Card front">
    <svg class="card-art" viewBox="0 0 540 309" aria-hidden="true">
      <path d="M0 24 Q270 10 540 -4 L540 5 Q270 22 0 31 Z" fill="var(--navy)"/>
      <path d="M0 36 Q270 26 540 10" fill="none" stroke="var(--light-sky)" stroke-width="1.5"/>
      <path d="M0 296 Q230 246 540 246 L540 254 Q250 258 30 309 L0 309 Z" fill="var(--navy)"/>
      <path d="M44 309 Q260 264 540 260" fill="none" stroke="var(--light-sky)" stroke-width="3"/>
    </svg>
    <div class="brand"><span class="brand-mark"></span>Orvek Electric Construction</div>
  </section>

  <section class="card card-back" aria-label="Card back">
    <svg class="card-art" viewBox="0 0 540 309" aria-hidden="true">
      <path d="M0 138 C200 123 380 83 540 33" fill="none" stroke="var(--light-sky)" stroke-width="6"/>
      <path d="M0 148 C200 133 380 93 540 45 L540 258 C380 270 200 290 120 309 L0 309 Z" fill="var(--navy)"/>
      <path d="M150 309 C240 290 400 274 540 268" fill="none" stroke="var(--sky)" stroke-width="9"/>
      <path d="M180 309 C270 294 420 284 540 282" fill="none" stroke="var(--light-sky)" stroke-width="3"/>
    </svg>

    <div class="brand"><span class="brand-mark"></span>Orvek Electric Construction</div>

    <ul class="contact-list">
      <li>
        <svg class="contact-icon" viewBox="0 0 12 12" aria-hidden="true"><path d="M2.5 0.5 L4.5 0.5 L5 3 L3.8 4.1 C4.5 5.7 6.3 7.5 7.9 8.2 L9 7 L11.5 7.5 L11.5 9.5 C11.5 10.6 10.6 11.5 9.5 11.5 C4.5 11.2 0.8 7.5 0.5 2.5 C0.5 1.4 1.4 0.5 2.5 0.5 Z"/></svg>
        <span>+61 400 517 382</span>
      </li>
      <li>
        <svg class="contact-icon" viewBox="0 0 12 12" aria-hidden="true"><path d="M0.5 2 H11.5 V10 H0.5 Z M1.2 2.6 L6 6.6 L10.8 2.6" fill="none" stroke="#fff" stroke-width="1.2"/></svg>
        <span>hello@orvekelectric.com.au</span>
      </li>
      <li>
        <svg class="contact-icon" viewBox="0 0 12 12" aria-hidden="true"><path d="M6 0.8 L11.5 5.8 L9.8 5.8 L9.8 11.2 L7.3 11.2 L7.3 7.8 L4.7 7.8 L4.7 11.2 L2.2 11.2 L2.2 5.8 L0.5 5.8 Z"/></svg>
        <span>42 Harbour Lane Melbourne VIC<br>3000 Australia</span>
      </li>
    </ul>

    <div class="holder">
      <p class="holder-name">Dana Whitfield</p>
      <p class="holder-role">Director</p>
    </div>
  </section>

</body>
</html>
```